Beacon Advisory Website

I currently have a website www.beaconadvisoryinc.example. We are a IT Consulting Company. Our website will pretty much tell out our services. I am looking to enhance my website and make it look more professional. Looking for very classy and Contemporary look and design for my website.

Industry/Entity Type

It Company

```html
<!DOCTYPE html>
<html lang="en">
<head>
<meta charset="utf-8">
<title>Beacon Advisory – IT Consulting</title>
<link rel="stylesheet" href="https://fonts.googleapis.com/css2?family=Open+Sans:wght@300;400;600;700&family=Poppins:wght@400;500;600&display=swap">
<style>
:root{
  --brand:#1a5a9a;
  --brand-dark:#0f3f7a;
  --accent:#1fb0e6;
  --cyan:#26b7d4;
  --ink:#262626;
  --body:#555;
  --line:#d9dde3;
  --card:#eef0f4;
  --footer:#272727;
  --footer-bottom:#1d1d1d;
  --footer-text:#a9a9a9;
  --white:#fff;
}
*{box-sizing:border-box;margin:0;padding:0}
html,body{width:1200px;height:2550px;overflow:hidden}
body{position:relative;font-family:"Open Sans",Arial,sans-serif;color:var(--body);background:var(--white)}
.abs{position:absolute}

/* Header */
.site-header{position:absolute;left:0;top:0;width:1200px;height:80px;background:rgba(255,255,255,.93);z-index:5}
.brand{position:absolute;left:92px;top:22px;display:flex;align-items:center;gap:12px}
.brand-mark{width:34px;height:34px;background:var(--brand)}
.brand-name{font-size:22px;font-weight:700;color:var(--brand);letter-spacing:.3px}
.main-nav{position:absolute;right:0;top:0;height:80px;display:flex}
.main-nav a{display:block;height:80px;line-height:80px;font-size:14px;color:#222;text-decoration:none;text-transform:uppercase;margin-right:52px;position:relative}
.main-nav a.active::after{content:"";position:absolute;left:-6px;right:-6px;bottom:0;height:4px;background:var(--brand)}

/* Hero */
.hero{position:absolute;left:0;top:0;width:1200px;height:620px;background:linear-gradient(110deg,#3d4e5c 0%,#8a9aa8 30%,#c9d3da 55%,#7d8d9b 80%,#3f4f5d 100%)}
.hero-caption{position:absolute;left:88px;top:212px;width:407px;height:243px;background:rgba(26,95,170,.88);padding:16px 16px 0 16px;color:var(--white)}
.hero-kicker{font-size:22px;font-weight:300;color:#4fc3f7}
.hero-title{font-size:34px;font-weight:700;line-height:1.3;margin-top:2px}
.hero-text{font-size:16px;line-height:1.4;margin-top:6px}
.hero-stat{margin-top:10px;display:flex;align-items:baseline;gap:12px}
.hero-stat small{font-size:19px;color:#4fc3f7;font-weight:400;margin-left:8px}
.hero-stat strong{font-size:58px;font-weight:700;line-height:1}
.slider-arrow{position:absolute;top:283px;width:48px;height:76px;background:rgba(40,40,40,.8);display:flex;align-items:center;justify-content:center}
.slider-arrow.prev{left:0}.slider-arrow.next{right:0}

/* Section headings */
.section-title{position:absolute;left:0;width:1200px;text-align:center;font-weight:700;font-size:46px;color:var(--ink)}
.divider{position:absolute;height:1px;background:var(--line)}
.divider-mark{position:absolute;width:20px;height:20px;background:var(--accent);border-radius:3px}

/* Services */
.service{position:absolute;width:300px;text-align:center}
.service-icon{width:108px;height:108px;border-radius:50%;background:var(--accent);margin:0 auto;display:flex;align-items:center;justify-content:center}
.service.featured .service-icon{background:var(--brand-dark)}
.service h3{font-size:22px;font-weight:400;color:#333;margin-top:28px}
.service.featured h3{color:var(--brand)}
.service p{font-size:13.5px;line-height:1.65;color:#555;margin-top:18px}
.read-more{display:inline-block;font-size:12.5px;color:#222;margin-top:16px;padding:4px 10px}
.service.featured .read-more{border:1px solid var(--brand);color:var(--brand)}

/* Vision */
.vision{position:absolute;left:0;top:1163px;width:1200px;height:498px;background:linear-gradient(180deg,#1b5c9c,#15558f)}
.vision .section-title{color:var(--white);font-size:44px;top:30px}
.vision-text{position:absolute;left:94px;top:162px;width:540px;font-size:15px;line-height:1.65;color:var(--white)}
.vision-list{position:absolute;left:94px;top:286px;list-style:none}
.vision-list li{display:flex;align-items:center;gap:14px;color:var(--white);font-size:15px;height:45px}
.tick{width:22px;height:22px;border-radius:50%;background:#3ea8dc;display:flex;align-items:center;justify-content:center}
.laptop{position:absolute;left:612px;top:155px;width:455px;height:284px}
.laptop-screen{position:absolute;left:39px;top:0;width:377px;height:260px;background:#1b1b1b;border-radius:12px 12px 0 0;padding:16px}
.laptop-display{width:100%;height:100%;background:linear-gradient(160deg,#d6dde4,#8d9aa6 60%,#4c5866)}
.laptop-base{position:absolute;left:0;top:258px;width:455px;height:18px;background:linear-gradient(#e4e6e8,#a9adb1);border-radius:0 0 40px 40px}

/* Testimonials */
.testimonial{position:absolute;top:1848px;width:490px}
.quote{background:var(--card);height:104px;padding:12px 22px;font-size:13px;line-height:1.6;text-align:center;color:#555}
.author{position:absolute;top:82px;left:12px;display:flex;align-items:center;gap:20px}
.avatar{width:88px;height:88px;border-radius:50%;border:3px solid var(--white);background:linear-gradient(160deg,#b9a08a,#6b5a4e)}
.author-name{font-family:"Poppins",sans-serif;font-size:13px;font-weight:500;color:#333;margin-top:28px}
.author-role{font-family:"Poppins",sans-serif;font-size:12px;color:#777;margin-top:6px}

/* Footer */
.site-footer{position:absolute;left:0;top:2163px;width:1200px;height:337px;background:var(--footer);font-family:"Poppins",sans-serif}
.footer-col{position:absolute;top:36px;width:240px}
.footer-col h4{font-size:14px;font-weight:600;color:var(--white);text-transform:uppercase;margin-top:0}
.footer-brand{display:flex;align-items:center;gap:10px}
.footer-brand .brand-mark{width:30px;height:30px}
.footer-brand .brand-name{color:var(--white);font-size:19px}
.footer-about{font-family:"Open Sans",sans-serif;font-size:12.5px;line-height:1.75;color:var(--footer-text);margin-top:18px}
.social{display:flex;gap:10px;margin-top:26px}
.social span{width:28px;height:28px;border-radius:50%;background:#5a5a5a}
.contact-list,.link-list{list-style:none;margin-top:28px}
.contact-list li{display:flex;gap:12px;font-size:11.5px;color:var(--footer-text);margin-bottom:18px;line-height:1.6}
.contact-list svg{flex:none;margin-top:3px}
.link-list li{font-size:12px;color:var(--footer-text);margin-bottom:17px}
.link-list li::before{content:"›";color:var(--cyan);margin-right:10px}
.newsletter p{font-size:12.5px;line-height:1.8;color:var(--footer-text);margin-top:26px}
.email-field{margin-top:16px;height:44px;border:1px solid #444;padding:0 16px;line-height:42px;font-size:13px;color:#ddd}
.signup{margin-top:19px;height:42px;background:var(--cyan);color:var(--white);text-align:center;line-height:42px;font-size:13px;font-weight:500}
.copyright{position:absolute;left:0;top:2500px;width:1200px;height:50px;background:var(--footer-bottom);color:#ccc;text-align:center;line-height:50px;font-size:13px}
</style>
</head>
<body>

<section class="hero" role="img" aria-label="Photo of three smiling colleagues working together at laptops in a bright office">
  <div class="hero-caption">
    <p class="hero-kicker">Today's IT market is a Dynamic</p>
    <h1 class="hero-title">FAST-PACED INDUSTRY</h1>
    <p class="hero-text">Fast-paced industry, with ever-increasing demands. Meeting these demands.</p>
    <p class="hero-stat"><small>OVER</small><strong>25 years</strong></p>
  </div>
  <div class="slider-arrow prev"><svg width="16" height="28" viewBox="0 0 16 28"><path d="M14 2 2 14l12 12" fill="none" stroke="#fff" stroke-width="2"/></svg></div>
  <div class="slider-arrow next"><svg width="16" height="28" viewBox="0 0 16 28"><path d="M2 2l12 12L2 26" fill="none" stroke="#fff" stroke-width="2"/></svg></div>
</section>

<header class="site-header">
  <div class="brand"><span class="brand-mark"></span><span class="brand-name">Beacon Advisory</span></div>
  <nav class="main-nav">
    <a class="active">Home</a><a>Services</a><a>Solutions</a><a>Resources</a><a>Career</a><a>Contact Us</a>
  </nav>
</header>

<!-- Who we are -->
<h2 class="section-title" style="top:652px">Who We Are</h2>
<div class="divider" style="left:245px;top:733px;width:743px"></div>
<div class="divider-mark" style="left:590px;top:723px"></div>

<div class="service" style="left:80px;top:784px">
  <div class="service-icon"><svg width="54" height="46" viewBox="0 0 54 46" fill="none" stroke="#fff" stroke-width="2.5"><rect x="12" y="2" width="38" height="26" rx="2"/><path d="M6 8v24h28l8 8v-8h4" /><rect x="4" y="8" width="36" height="24" rx="2" fill="var(--accent)"/><path d="M12 32v10l8-10"/></svg></div>
  <h3>Consulting</h3>
  <p>Beacon Advisory has certified professional consultants to work with you to help increase the business by providing IT services ...</p>
  <span class="read-more">Read more →</span>
</div>

<div class="service featured" style="left:450px;top:784px">
  <div class="service-icon"><svg width="56" height="56" viewBox="0 0 56 56" fill="none" stroke="#fff" stroke-width="2.5"><circle cx="28" cy="24" r="20"/><circle cx="28" cy="24" r="13"/><circle cx="28" cy="20" r="5" fill="#fff"/><path d="M19 36c2-7 16-7 18 0" fill="#fff"/></svg></div>
  <h3>Staff Augmentation</h3>
  <p>For years Beacon Advisory as been offering our customers the ability to augment their existing staff ...</p>
  <span class="read-more">Read more →</span>
</div>

<div class="service" style="left:778px;top:784px">
  <div class="service-icon"><svg width="56" height="56" viewBox="0 0 56 56" fill="none" stroke="#fff" stroke-width="3"><path d="M24 6h8l2 6 5 3 6-2 4 7-5 4v6l5 4-4 7-6-2-5 3-2 6h-8l-2-6-5-3-6 2-4-7 5-4v-6l-5-4 4-7 6 2 5-3z"/><circle cx="28" cy="28" r="7"/></svg></div>
  <h3>Offshore</h3>
  <p>For years Beacon Advisory as been offering our customers the ability to augment their existing staff ...</p>
  <span class="read-more">Read more →</span>
</div>

<!-- Vision -->
<section class="vision">
  <h2 class="section-title">Vision &amp; Mission</h2>
  <div class="divider" style="left:230px;top:109px;width:748px;background:rgba(255,255,255,.3)"></div>
  <div class="divider-mark" style="left:576px;top:99px"></div>
  <p class="vision-text">Through the commitment of our employees and innovative engineering, we provide highly-reliable flexible circuits, heaters, sensors, instruments, integrated products and services that maximize our customers' competitive advantage.</p>
  <ul class="vision-list">
    <li><span class="tick"><svg width="12" height="10" viewBox="0 0 12 10"><path d="M1 5l3.5 3.5L11 1" fill="none" stroke="#fff" stroke-width="2"/></svg></span>Delivering real value to our clients by providing top quality.</li>
    <li><span class="tick"><svg width="12" height="10" viewBox="0 0 12 10"><path d="M1 5l3.5 3.5L11 1" fill="none" stroke="#fff" stroke-width="2"/></svg></span>Delivering real value to shareholders through consistent growth.</li>
    <li><span class="tick"><svg width="12" height="10" viewBox="0 0 12 10"><path d="M1 5l3.5 3.5L11 1" fill="none" stroke="#fff" stroke-width="2"/></svg></span>Delivering the best work environment for our consultants and staff</li>
  </ul>
  <div class="laptop">
    <div class="laptop-screen"><div class="laptop-display" role="img" aria-label="Photo of a business team meeting around a conference table with charts on a wall screen"></div></div>
    <div class="laptop-base"></div>
  </div>
</section>

<!-- Testimonials -->
<h2 class="section-title" style="top:1695px">Testimonials</h2>
<div class="divider" style="left:230px;top:1775px;width:745px"></div>
<div class="divider-mark" style="left:576px;top:1765px"></div>

<article class="testimonial" style="left:96px">
  <p class="quote">We have several sites now built in Lumora across several servers and have had almost zero issues. The documentation is great and the feature set is phenomenal...</p>
  <div class="author">
    <div class="avatar" role="img" aria-label="Portrait photo of a male client"></div>
    <div><p class="author-name">Daniel Harper</p><p class="author-role">Cobalt Ridge Co. CEO</p></div>
  </div>
</article>

<article class="testimonial" style="left:604px">
  <p class="quote">We have several sites now built in Lumora across several servers and have had almost zero issues. The documentation is great and the feature set is phenomenal...</p>
  <div class="author">
    <div class="avatar" role="img" aria-label="Portrait photo of a female client" style="background:linear-gradient(160deg,#c9b3a3,#5d4a40)"></div>
    <div><p class="author-name">Laura Bennett</p><p class="author-role">Cobalt Ridge Co. CEO</p></div>
  </div>
</article>

<!-- Footer -->
<footer class="site-footer">
  <div class="footer-col" style="left:90px;top:26px">
    <div class="footer-brand"><span class="brand-mark"></span><span class="brand-name">Beacon Advisory</span></div>
    <p class="footer-about">Today's IT market is a dynamic, fast-paced industry, with ever-increasing demands. Meeting these demands for over 25 years, Beacon Advisory maintains a global presence,</p>
    <div class="social"><span></span><span></span><span></span><span></span></div>
  </div>
  <div class="footer-col" style="left:353px">
    <h4>Get in touch</h4>
    <ul class="contact-list">
      <li><svg width="10" height="13" viewBox="0 0 10 13"><path d="M5 0a5 5 0 0 0-5 5c0 4 5 8 5 8s5-4 5-8a5 5 0 0 0-5-5z" fill="var(--cyan)"/><circle cx="5" cy="5" r="2" fill="var(--footer)"/></svg>880 Harbor Ave. Fairmont, CA 95012<br>United States</li>
      <li><svg width="12" height="12" viewBox="0 0 12 12"><path d="M2 0l3 3-1.5 2a8 8 0 0 0 3.5 3.5L9 7l3 3-2 2C5 12 0 7 0 2z" fill="var(--cyan)"/></svg>(555) 01234567</li>
      <li><svg width="12" height="12" viewBox="0 0 12 12"><path d="M0 5 12 0 9 12 6 8z" fill="var(--cyan)"/></svg>info@beaconadvisory.example</li>
      <li><svg width="9" height="13" viewBox="0 0 9 13"><rect x="1" y="1" width="7" height="11" rx="1.5" fill="none" stroke="var(--cyan)" stroke-width="1.6"/></svg>(555) 01234567</li>
      <li><svg width="12" height="12" viewBox="0 0 12 12"><circle cx="6" cy="6" r="5" fill="none" stroke="var(--cyan)" stroke-width="1.6"/><path d="M6 3v3l2 1.5" fill="none" stroke="var(--cyan)" stroke-width="1.4"/></svg>Mon - Sat: 9:00 - 18:00</li>
    </ul>
  </div>
  <div class="footer-col" style="left:616px">
    <h4>Information</h4>
    <ul class="link-list"><li>Home</li><li>Services</li><li>Solutions</li><li>Resources</li><li>Career</li><li>Contact Us</li></ul>
  </div>
  <div class="footer-col newsletter" style="left:879px;width:237px">
    <h4>News letter</h4>
    <p>Enter your email address for our mailing list to keep your self our lastest updated.</p>
    <div class="email-field">Email</div>
    <div class="signup">Sign up</div>
  </div>
</footer>
<div class="copyright">Copyright © 2007 - 2016 Beacon Advisory Ltd.&nbsp; All Rights Reserved</div>

</body>
</html>
```